Escape Room Flyer Design - Start up. A5

Flyer is for letterbox drops to get interest and let people know that our business exists and to a lesser extent what an escape room is. We have 1 room (the miller's shadows) and a second room coming soon (Varuna's Vault). I have attached our logo and 2 flyers that I have seen in the past that I really like the design of.
Whether you are having a night out with friends or family, celebrating a special event, planning a team-building activity, or simply wanting a diversion from the doldrums of your workweek, The Lock Box will provide you an unforgettable live-action gaming experience.

Target Market(s)

18-25

Industry/Entity Type

Entertainment

Requirements
Must have
• Logo. Phone number 0417 265 839. Website. www.thelockboxhartwell.com
Bookings essential.
Nice to have
• Mystery, a little bit on the darker side than bright colourful and blocky.
"Many Will Enter…Few Will Escape" tag line
60 minute game. Team work. 2-6 players. All ages.
Should not have
• Cartoons, characters, people

```html
<!DOCTYPE html>
<html lang="en">
<head>
<meta charset="utf-8">
<title>The Lock Box – Escape Room Flyer</title>
<link href="https://fonts.googleapis.com/css2?family=Permanent+Marker&family=Gochi+Hand&family=Montserrat:wght@400;500;800&family=Arimo:wght@400;700&display=swap" rel="stylesheet">
<style>
  :root {
    --ink: #0b0b0b;
    --ink-soft: #1c1c1c;
    --gold: #f0c419;
    --paper: #ffffff;
    --stage: #dcdcdc;
  }
  * { margin: 0; padding: 0; box-sizing: border-box; }
  html, body { width: 960px; height: 1200px; overflow: hidden; }
  body { background: var(--stage); position: relative; }

  .flyer {
    position: absolute; left: 57px; top: 0;
    width: 846px; height: 1200px;
    background: var(--ink); overflow: hidden;
    color: var(--paper);
  }
  .flyer__texture {
    position: absolute; inset: 0;
    background: radial-gradient(circle at 50% 48%, #262626 0%, #161616 35%, var(--ink) 75%);
  }
  .flyer__border { position: absolute; inset: 0; width: 846px; height: 1200px; }

  .brand {
    position: absolute; left: 0; right: 0; top: 118px;
    display: flex; justify-content: center; align-items: center; gap: 10px;
  }
  .brand__mark { width: 22px; height: 22px; background: var(--gold); }
  .brand__name {
    font-family: "Montserrat", sans-serif; font-weight: 800;
    font-size: 30px; letter-spacing: 2px; color: var(--gold); text-transform: uppercase;
  }

  .tagline__lead {
    position: absolute; left: 0; right: 0; top: 262px; text-align: center;
    font-family: "Gochi Hand", cursive; font-size: 64px; line-height: 1;
  }
  .tagline__main {
    position: absolute; left: 0; right: 0; top: 342px; text-align: center;
    font-family: "Permanent Marker", cursive; color: var(--gold);
    font-size: 120px; line-height: 0.98; letter-spacing: 2px;
  }

  .icon-key { position: absolute; left: 690px; top: 78px; width: 110px; height: 190px; }
  .icon-lock { position: absolute; left: 34px; top: 604px; width: 60px; height: 68px; transform: rotate(14deg); }

  .intro__label {
    position: absolute; left: 282px; top: 629px; width: 282px; height: 35px;
    background: var(--gold); color: var(--ink);
    font-family: "Arimo", sans-serif; font-weight: 700; font-size: 17px;
    display: flex; align-items: center; justify-content: center;
  }
  .intro__copy {
    position: absolute; left: 100px; width: 646px; text-align: center;
    font-family: "Montserrat", sans-serif; font-weight: 400;
  }
  .intro__copy--first { top: 684px; font-size: 14.5px; line-height: 19.5px; }
  .intro__copy--second { top: 762px; font-size: 12.6px; line-height: 17px; }

  .features { position: absolute; left: 0; top: 860px; width: 846px; height: 180px; }
  .feature { position: absolute; width: 140px; text-align: center; }
  .feature__hex { display: block; margin: 0 auto; width: 104px; height: 118px; }
  .feature__label {
    margin-top: 18px;
    font-family: "Montserrat", sans-serif; font-weight: 800;
    font-size: 17px; line-height: 22px; text-transform: uppercase;
  }
  .feature--players { left: 74px; }
  .feature--time { left: 352px; }
  .feature--adventure { left: 624px; }
  .features__arrow { position: absolute; width: 70px; height: 50px; }

  .booking {
    position: absolute; left: 0; right: 0; top: 1054px; text-align: center;
    font-family: "Arimo", sans-serif; font-size: 39px; color: var(--gold);
  }
  .contact {
    position: absolute; left: 0; right: 0; top: 1114px;
    display: flex; justify-content: center; align-items: center;
    font-family: "Arimo", sans-serif;
  }
  .contact__icon { width: 24px; height: 24px; margin-right: 6px; }
  .contact__phone { font-size: 30px; margin-right: 16px; }
  .contact__web { font-size: 17px; }
</style>
</head>
<body>
<main class="flyer">
  <div class="flyer__texture" role="img" aria-label="Faint maze and cobweb background texture"></div>

  <svg class="flyer__border" viewBox="0 0 846 1200">
    <g fill="#f0c419">
      <polygon role="img" aria-label="Greek key border ornament, top left corner" points="0,85 210,0 298,0 0,171"/>
      <polygon role="img" aria-label="Greek key border ornament, top right corner" points="647,0 724,0 846,112 846,200"/>
      <polygon role="img" aria-label="Greek key border ornament, bottom left corner" points="0,995 206,1200 88,1200 0,1104"/>
      <polygon role="img" aria-label="Greek key border ornament, bottom right corner" points="846,995 640,1200 751,1200 846,1104"/>
    </g>
  </svg>

  <div class="brand">
    <span class="brand__mark"></span>
    <span class="brand__name">The Lock Box</span>
  </div>

  <svg class="icon-key" viewBox="0 0 110 190" aria-hidden="true">
    <g fill="none" stroke="#fff" stroke-width="10" stroke-linecap="round">
      <circle cx="68" cy="42" r="36"/>
      <line x1="56" y1="78" x2="10" y2="180"/>
      <line x1="30" y1="136" x2="56" y2="146"/>
      <line x1="22" y1="156" x2="46" y2="166"/>
    </g>
  </svg>

  <svg class="icon-lock" viewBox="0 0 60 68" aria-hidden="true">
    <path d="M16 30 V20 a14 14 0 0 1 28 0" fill="none" stroke="#fff" stroke-width="6"/>
    <rect x="4" y="28" width="52" height="38" rx="6" fill="#fff"/>
    <circle cx="30" cy="44" r="5" fill="#0b0b0b"/>
    <rect x="28" y="44" width="4" height="12" fill="#0b0b0b"/>
  </svg>

  <p class="tagline__lead">Many Will Enter</p>
  <h1 class="tagline__main">FEW WILL<br>ESCAPE</h1>

  <h2 class="intro__label">WHAT IS AN ESCAPE ROOM</h2>
  <p class="intro__copy intro__copy--first">We are a family owned, built, operated and created escape room unique to the region. Having done Escape Rooms all over the world, we wanted to bring our own flavor back home to share with our region.</p>
  <p class="intro__copy intro__copy--second">With the help of our team, we have designed and built the rooms, decorations and puzzles ourselves so that we can have full control over the experience we provide. We are very proud of what we have accomplished and we hope to continue to create new adventures for many years to come.</p>

  <section class="features">
    <div class="feature feature--players">
      <svg class="feature__hex" viewBox="0 0 104 118">
        <polygon points="52,3 101,31 101,87 52,115 3,87 3,31" fill="none" stroke="#f0c419" stroke-width="4"/>
        <circle role="img" aria-label="Group of players icon" cx="52" cy="59" r="22" fill="#3a3220"/>
      </svg>
      <p class="feature__label">2 to 6<br>players</p>
    </div>
    <svg class="features__arrow" style="left:255px;top:40px" viewBox="0 0 70 50" aria-hidden="true">
      <path d="M4 8 Q28 40 62 32 M50 22 L63 32 L50 42" fill="none" stroke="#f0c419" stroke-width="3" stroke-linecap="round"/>
    </svg>
    <div class="feature feature--time">
      <svg class="feature__hex" viewBox="0 0 104 118">
        <polygon points="52,3 101,31 101,87 52,115 3,87 3,31" fill="none" stroke="#f0c419" stroke-width="4"/>
        <g fill="none" stroke="#f0c419" stroke-width="2.5" stroke-linecap="round">
          <circle cx="52" cy="36" r="6"/><line x1="52" y1="42" x2="52" y2="58"/><line x1="52" y1="52" x2="57" y2="52"/>
          <circle cx="44" cy="66" r="6"/><line x1="40" y1="70" x2="30" y2="82"/>
          <circle cx="62" cy="68" r="6"/><line x1="66" y1="72" x2="76" y2="84"/>
        </g>
      </svg>
      <p class="feature__label">60 minutes<br>of game</p>
    </div>
    <svg class="features__arrow" style="left:532px;top:36px" viewBox="0 0 70 50" aria-hidden="true">
      <path d="M4 42 Q22 14 62 14 M50 4 L63 14 L50 24" fill="none" stroke="#f0c419" stroke-width="3" stroke-linecap="round"/>
    </svg>
    <div class="feature feature--adventure">
      <svg class="feature__hex" viewBox="0 0 104 118">
        <polygon points="52,3 101,31 101,87 52,115 3,87 3,31" fill="none" stroke="#f0c419" stroke-width="4"/>
        <circle role="img" aria-label="Dragon adventure icon" cx="52" cy="59" r="22" fill="#3a3220"/>
      </svg>
      <p class="feature__label">Tons of<br>adventure</p>
    </div>
  </section>

  <p class="booking">BOOKINGS ESSENTIAL</p>

  <div class="contact">
    <svg class="contact__icon" viewBox="0 0 24 24" aria-hidden="true">
      <path d="M6 2 L10 7 L8 10 C9 13 11 15 14 16 L17 14 L22 18 L19 22 C10 21 3 14 2 5 Z" fill="#f0c419"/>
    </svg>
    <span class="contact__phone">0417 265 839</span>
    <svg class="contact__icon" viewBox="0 0 24 24" aria-hidden="true">
      <g fill="none" stroke="#f0c419" stroke-width="2">
        <circle cx="12" cy="12" r="10"/><ellipse cx="12" cy="12" rx="4.5" ry="10"/>
        <line x1="2" y1="12" x2="22" y2="12"/><line x1="4" y1="7" x2="20" y2="7"/><line x1="4" y1="17" x2="20" y2="17"/>
      </g>
    </svg>
    <span class="contact__web">www.thelockboxhartwell.com</span>
  </div>
</main>
</body>
</html>
```